Kestrel Roofing & Restoration Business Card Design

Lookiing for a double sided business card design that will have rounded corners, will look good with Spot UV, Soft Laminate, or Gloss
Front of card should have Logo, Name and Contact Info, License numbers
Back of card should have Logo, maybe other small details

```html
<!DOCTYPE html>
<html lang="en">
<head>
<meta charset="utf-8">
<title>Kestrel Roofing &amp; Restoration — Business Cards</title>
<link href="https://fonts.googleapis.com/css2?family=Poppins:wght@400;600&family=Nunito:wght@900&family=Inter:wght@400&family=Space+Mono:ital,wght@1,700&display=swap" rel="stylesheet">
<style>
  :root {
    --page: #c4cde0;
    --navy: #030b57;
    --navy-deep: #020a50;
    --royal: #010d72;
    --line: #ffffff;
    --ink: #ffffff;
    --rule-blue: #4a63c9;
  }
  * { margin: 0; padding: 0; box-sizing: border-box; }
  html, body { width: 1200px; height: 800px; overflow: hidden; }
  body { background: var(--page); position: relative; font-family: "Poppins", sans-serif; color: var(--ink); }

  .card {
    position: absolute;
    left: 346px;
    width: 500px;
    height: 286px;
    background: var(--navy);
    border-radius: 8px;
    overflow: hidden;
  }
  .card--back { top: 81px; }
  .card--front { top: 436px; }
  .card__grid { position: absolute; inset: 0; width: 100%; height: 100%; }

  .wordmark { position: absolute; font-family: "Poppins", sans-serif; font-weight: 600; color: var(--ink); letter-spacing: 0.02em; }

  /* back side */
  .card--back .wordmark__name { position: absolute; right: 164px; top: 160px; font-size: 22px; line-height: 1; }
  .card--back .wordmark__divider { position: absolute; left: 343px; top: 155px; width: 1px; height: 40px; background: var(--line); opacity: .8; }
  .card--back .wordmark__tag { position: absolute; left: 351px; top: 152px; font-size: 17px; line-height: 22px; }

  /* front side */
  .card--front .wordmark { left: 322px; top: 0; width: 177px; text-align: center; }
  .card--front .wordmark__name { display: block; margin-top: 40px; font-size: 28px; line-height: 1; }
  .card--front .wordmark__rule { display: block; width: 77px; height: 2px; background: var(--rule-blue); margin: 18px auto 0; }
  .card--front .wordmark__tag { display: block; margin-top: 6px; font-size: 17px; line-height: 22px; }

  .contact { position: absolute; left: 27px; top: 108px; }
  .contact__name { font-family: "Nunito", sans-serif; font-weight: 900; font-size: 29px; line-height: 34px; letter-spacing: -0.01em; }
  .contact__line { font-family: "Inter", sans-serif; font-size: 15px; line-height: 20px; }
  .contact__line--phone { margin-top: 7px; letter-spacing: 0.04em; }
  .contact__license { font-family: "Space Mono", monospace; font-style: italic; font-weight: 700; font-size: 16px; letter-spacing: 0.06em; margin-top: 26px; }
</style>
</head>
<body>

  <section class="card card--back" aria-label="Card back">
    <svg class="card__grid" viewBox="0 0 780 446" preserveAspectRatio="none" aria-hidden="true">
      <defs>
        <linearGradient id="glowTop" x1="0" y1="0" x2="1" y2="0">
          <stop offset="0" stop-color="#010c6e"/>
          <stop offset="1" stop-color="#030a55"/>
        </linearGradient>
        <linearGradient id="glowLeft" x1="0" y1="0" x2="1" y2="1">
          <stop offset="0" stop-color="#030a55"/>
          <stop offset="1" stop-color="#010c6e"/>
        </linearGradient>
      </defs>
      <rect width="780" height="446" fill="#030b57"/>
      <rect x="376" y="0" width="404" height="118" fill="url(#glowTop)"/>
      <rect x="0" y="0" width="125" height="329" fill="url(#glowLeft)"/>
      <rect x="125" y="0" width="251" height="118" fill="#020a50"/>
      <g stroke="#ffffff" stroke-width="2" fill="none">
        <line x1="125" y1="0" x2="125" y2="446"/>
        <line x1="376" y1="0" x2="376" y2="446"/>
        <polyline points="780,118 249,118 249,329 0,329"/>
      </g>
    </svg>
    <div class="wordmark">
      <span class="wordmark__name">KESTREL</span>
    </div>
    <span class="wordmark__divider"></span>
    <div class="wordmark"><span class="wordmark__tag">ROOFING &amp;<br>RESTORATION</span></div>
  </section>

  <section class="card card--front" aria-label="Card front">
    <svg class="card__grid" viewBox="0 0 778 444" preserveAspectRatio="none" aria-hidden="true">
      <defs>
        <linearGradient id="bandTop" x1="0" y1="0" x2="1" y2="0">
          <stop offset="0" stop-color="#030b5c"/>
          <stop offset="1" stop-color="#010d72"/>
        </linearGradient>
      </defs>
      <rect width="778" height="444" fill="#020a50"/>
      <rect x="0" y="0" width="502" height="118" fill="url(#bandTop)"/>
      <rect x="502" y="0" width="276" height="262" fill="#030b57"/>
      <rect x="502" y="262" width="276" height="182" fill="#010d72"/>
      <g stroke="#ffffff" stroke-width="2" fill="none">
        <line x1="62" y1="0" x2="62" y2="118"/>
        <polyline points="0,118 502,118 502,262 778,262"/>
      </g>
    </svg>
    <div class="wordmark">
      <span class="wordmark__name">KESTREL</span>
      <span class="wordmark__rule"></span>
      <span class="wordmark__tag">ROOFING &amp;<br>RESTORATION</span>
    </div>
    <div class="contact">
      <h1 class="contact__name">Marcus Hale</h1>
      <p class="contact__line contact__line--phone">021 555 0148</p>
      <p class="contact__line">info@kestrelroofing.com</p>
      <p class="contact__license">4870261935</p>
    </div>
  </section>

</body>
</html>
```